Robotic startup business cards

We are looking for a design for a set of business cards which reflect the spirit and humor of Vortalo Robotics. We want to present ourselves as sleek, professional, but laid-back consulting company.

We primarily focus on developing robotic arms software. This software controls robots and does things like grab items, pick objects up, move them, etc.

We want to allow you maximum design creativity, but do ask that you consider our existing style guidelines (see attached files) in order to make our brand cohesive.

Target Market(s)

Startups and Mid-size robotic companies

Industry/Entity Type

Business

Contact Information for Business Card

Miro Halvensky, PhD
Roboticist | Vortalo Consulting | 318.570.9164

Font styles to use
Other font styles liked:
• Source code pro

Requirements
Must have
• robots or robotic arms
• similar color scheme that works with existing brand guidelines
Nice to have
• please consider our existing style guidelines (see attached files) in order to make our brand cohesive.
• minimalism style is generally nice.
Should not have
• An old, boring, or corporate feel. Too much text.

```html
<!DOCTYPE html>
<html lang="en">
<head>
<meta charset="utf-8">
<title>Vortalo Robotics – Business Card</title>
<link rel="stylesheet" href="https://fonts.googleapis.com/css2?family=Open+Sans:wght@400;600&family=Source+Code+Pro:wght@300&display=swap">
<style>
  :root {
    --backdrop: #6b4a33;
    --card: #232323;
    --card-shadow: rgba(0, 0, 0, 0.45);
    --silver: #d4d4d4;
    --accent: #5ccb9c;
    --text-light: #d8d8d8;
    --rule: #8a8a8a;
  }
  * { margin: 0; padding: 0; box-sizing: border-box; }
  html, body {
    width: 1200px;
    height: 1000px;
    overflow: hidden;
    background: var(--backdrop);
  }
  .canvas {
    position: relative;
    width: 1200px;
    height: 1000px;
  }
  .card {
    position: absolute;
    left: 266px;
    width: 666px;
    height: 397px;
    background: var(--card);
    box-shadow: 0 2px 8px var(--card-shadow);
  }
  .card--front { top: 74px; }
  .card--back { top: 533px; }

  .brand {
    position: absolute;
    left: 127px;
    top: 172px;
    display: flex;
    align-items: center;
    gap: 26px;
  }
  .brand__dot {
    width: 18px;
    height: 18px;
    border-radius: 50%;
    background: var(--silver);
  }
  .brand__name {
    font-family: "Source Code Pro", monospace;
    font-weight: 300;
    font-size: 46px;
    letter-spacing: 7px;
    color: var(--silver);
    line-height: 1;
  }

  .contact {
    position: absolute;
    left: 45px;
    top: 274px;
    width: 462px;
    font-family: "Open Sans", sans-serif;
  }
  .contact__title-row {
    display: flex;
    align-items: baseline;
    gap: 14px;
    padding-bottom: 9px;
    border-bottom: 1px solid var(--rule);
  }
  .contact__name {
    font-weight: 600;
    font-size: 17px;
    letter-spacing: 1.2px;
    color: var(--accent);
  }
  .contact__sep {
    font-size: 16px;
    color: var(--text-light);
  }
  .contact__role {
    font-size: 13px;
    letter-spacing: 1px;
    color: var(--text-light);
  }
  .contact__details {
    display: flex;
    gap: 11px;
    margin-top: 10px;
    font-size: 13px;
    letter-spacing: 0.8px;
    color: var(--text-light);
    white-space: nowrap;
  }
</style>
</head>
<body>
  <main class="canvas">
    <section class="card card--front">
      <div class="brand">
        <span class="brand__dot"></span>
        <span class="brand__name">VORTALO</span>
      </div>
    </section>

    <section class="card card--back">
      <div class="contact">
        <div class="contact__title-row">
          <span class="contact__name">MIRO HALVENSKY, PHD</span>
          <span class="contact__sep">\</span>
          <span class="contact__role">ROBOTICIST</span>
        </div>
        <div class="contact__details">
          <span>318.570.9164</span>
          <span>\</span>
          <span>INFO@VORTALO.COM</span>
          <span>\</span>
          <span>VORTALO CONSULTING</span>
        </div>
      </div>
    </section>
  </main>
</body>
</html>
```